Med Spa business card design with logo

Need a logo design and business card for our new company Velora Skinworks Med Spa. We are a medical office that deals with high end clients. We offer them skin care products which include NERVAX, lip augmentation, and various laser for the skin. I king of like the logo attached, maybe something along those lines but also open to any logo concept.
Updates

Target Market(s)

Out target audience are male and females in the age range of 21-80 years of age

Industry/Entity Type

Medical

Contact Information for Business Card

woukd like front of card to have logo and business name VELORA SKINWORKS MEDSPA. Back of card employee name and phone number along with instagram logo and user name

Font styles to use
Serif
Sans Serif

Requirements
Must have
• prefer monochromatic look white, black, gold
Should not have
• not too colorful

```html
<!DOCTYPE html>
<html lang="en">
<head>
<meta charset="utf-8">
<title>Velora Skinworks Med Spa – Business Cards</title>
<link rel="stylesheet" href="https://fonts.googleapis.com/css2?family=Open+Sans:wght@400;500&family=Arimo:wght@400&display=swap">
<style>
  :root {
    --backdrop: #c4c4c6;
    --card-white: #f5f5f5;
    --ink: #161616;
    --band: #111111;
    --panel-grey: #9b9898;
    --mark-grey: #8d8d8f;
  }
  html, body {
    margin: 0;
    width: 1200px;
    height: 1200px;
    overflow: hidden;
    background: var(--backdrop);
  }
  .canvas { position: relative; width: 1200px; height: 1200px; }
  .card { position: absolute; width: 714px; height: 408px; background: var(--card-white); overflow: hidden; }
  .card--contact { left: 172px; top: 154px; }
  .card--brand { left: 372px; top: 665px; width: 711px; }

  .brand-name {
    position: absolute;
    font-family: "Open Sans", sans-serif;
    font-weight: 400;
    color: var(--ink);
    text-align: center;
    margin: 0;
    white-space: nowrap;
  }
  .brand-mark { position: absolute; border-radius: 50%; background: var(--mark-grey); }

  .card--contact .brand-mark { left: 188px; top: 52px; width: 68px; height: 68px; }
  .card--contact .brand-name { left: 22px; width: 400px; top: 128px; font-size: 27px; line-height: 30px; letter-spacing: 0.5px; }

  .person { position: absolute; right: 57px; top: 120px; text-align: right; font-family: "Arimo", sans-serif; color: var(--ink); }
  .person__name { font-size: 24px; line-height: 28px; margin: 0; }
  .person__role { font-size: 16px; line-height: 20px; margin: 4px 0 0; }

  .band { position: absolute; left: 0; top: 190px; width: 100%; height: 32px; background: var(--band); }
  .panel { position: absolute; left: 0; top: 222px; width: 100%; bottom: 0; background: var(--panel-grey); }

  .contacts { position: absolute; font-family: "Arimo", sans-serif; font-size: 17px; line-height: 21px; color: var(--ink); list-style: none; margin: 0; padding: 0; }
  .contacts li { display: flex; align-items: center; gap: 10px; }
  .contacts--left { left: 70px; top: 298px; }
  .contacts--right { right: 58px; top: 319px; text-align: right; }
  .contacts--right li { justify-content: flex-end; }
  .icon { width: 13px; height: 13px; flex: none; display: block; }

  .divider { position: absolute; left: 370px; top: 307px; width: 3px; height: 55px; background: var(--band); }

  .card--brand .brand-mark { left: 302px; top: 131px; width: 104px; height: 104px; }
  .card--brand .brand-name { left: 0; width: 100%; top: 250px; font-size: 36px; line-height: 44px; letter-spacing: 0.6px; }
</style>
</head>
<body>
<main class="canvas">
  <section class="card card--contact">
    <div class="brand-mark"></div>
    <h1 class="brand-name">VELORA SKINWORKS<br>MEDSPA</h1>
    <div class="person">
      <p class="person__name">Daniel Reyes</p>
      <p class="person__role">Manager</p>
    </div>
    <div class="band"></div>
    <div class="panel"></div>
    <ul class="contacts contacts--left">
      <li><svg class="icon" viewBox="0 0 13 13"><rect width="13" height="13" fill="#161616"/><path d="M4 3 L5.5 3 L6 5 L5 5.8 Q6 7.8 7.4 8.4 L8.2 7.5 L10 8 L10 9.6 Q6 10.2 3.5 4.5 Z" fill="#9b9898"/></svg>415 555 0198</li>
      <li><svg class="icon" viewBox="0 0 13 13"><rect width="13" height="13" fill="#161616"/><rect x="3" y="5" width="7" height="5" fill="#9b9898"/><rect x="2.5" y="3" width="8" height="1.5" fill="#9b9898"/></svg>1-541-555-0142</li>
      <li><svg class="icon" viewBox="0 0 13 13"><rect width="13" height="13" fill="#161616"/><rect x="2.5" y="4" width="8" height="5.5" fill="#9b9898"/><path d="M2.5 4 L6.5 7 L10.5 4" stroke="#161616" stroke-width="1" fill="none"/></svg>info@velora.com</li>
    </ul>
    <div class="divider"></div>
    <ul class="contacts contacts--right">
      <li>www.veloraskin.com<svg class="icon" viewBox="0 0 13 13"><rect width="13" height="13" fill="#161616"/><circle cx="6.5" cy="6.5" r="3.6" fill="none" stroke="#9b9898" stroke-width="1.2"/><path d="M2.9 6.5 H10.1" stroke="#9b9898" stroke-width="1"/></svg></li>
      <li>veloraskinworks<svg class="icon" viewBox="0 0 13 13"><rect width="13" height="13" fill="#161616"/><path d="M6.5 11 L3.8 6.5 A3 3 0 1 1 9.2 6.5 Z" fill="#9b9898"/><circle cx="6.5" cy="5.3" r="1.1" fill="#161616"/></svg></li>
    </ul>
  </section>

  <section class="card card--brand">
    <div class="brand-mark"></div>
    <h2 class="brand-name">VELORA SKINWORKS MEDSPA</h2>
  </section>
</main>
</body>
</html>
```